Healthcare technology company needs website design

We need a logo for a new company based in the U.S. We develop software to assist consumers identifying lowest cost healthcare coverage methods, including insurance, discount cards, and cash options. We would like to see designs that use multiple shades of green with the optional addition of other complimentary colors. The final design should communicate a unique blend of saving money while receiving the healthcare you need.
Need the following pages/sections: Homepage, Solutions, About Us, Contact
Competitors: www.velorimed.example; www.qzplo.example

Target Market(s)

Businesses

Industry/Entity Type

Healthcare

Coding

Coded - Design and coding required

Number of Pages Required

4 page

Colors
0054AA
0677BA
7BADD7
CADEEF
E8F1F8
00AB8E
00BBA5
67D7C9
C6EFE9
E9F9F6

Requirements
Must have
• Matching color theme with logo
Nice to have
• Animated background

```html
<!DOCTYPE html>
<html lang="en">
<head>
<meta charset="utf-8">
<title>Fernbright Health</title>
<link href="https://fonts.googleapis.com/css2?family=Montserrat:wght@400;500;600;700&display=swap" rel="stylesheet">
<style>
:root{
  --blue-deep:#0054AA;
  --blue:#0677BA;
  --blue-mid:#7BADD7;
  --blue-soft:#CADEEF;
  --blue-pale:#E8F1F8;
  --green-deep:#00AB8E;
  --green:#00BBA5;
  --green-mid:#67D7C9;
  --green-soft:#C6EFE9;
  --green-pale:#E9F9F6;
  --ink:#1b1b1b;
  --white:#ffffff;
}
*{box-sizing:border-box;margin:0;padding:0}
html,body{width:1200px;height:3600px;overflow:hidden;background:var(--white)}
body{position:relative;font-family:'Montserrat',sans-serif;color:var(--ink)}
.abs{position:absolute}

/* header / hero */
.hero{left:0;top:0;width:1200px;height:600px;background:linear-gradient(100deg,#e9edf2 0%,#f1eeee 40%,#eef2f6 100%)}
.brand{left:42px;top:50px;display:flex;align-items:center;gap:22px}
.brand-mark{width:70px;height:70px;border-radius:50%;background:var(--green-deep)}
.brand-name{font-weight:700;font-size:42px;letter-spacing:1px;color:var(--green-deep)}
.nav{right:66px;top:32px;display:flex;gap:62px}
.nav a{font-weight:700;font-size:19px;color:var(--ink);text-decoration:none}
.hero-accent{left:52px;top:408px;width:11px;height:172px;background:var(--green-mid)}
.hero-title{left:98px;top:402px;font-size:50px;line-height:58px;font-weight:500;letter-spacing:3px;color:var(--ink)}

/* intro blocks */
.lead{left:141px;font-size:30px;line-height:36px;letter-spacing:1.5px;color:var(--blue-mid)}
.tri{width:112px;height:161px}
.btn{display:flex;align-items:center;justify-content:center;height:63px;border-radius:32px;background:linear-gradient(90deg,var(--green-deep),var(--green-mid));color:var(--white);font-size:34px;letter-spacing:3px;box-shadow:0 3px 6px rgba(0,0,0,.18)}
.more{display:flex;align-items:center;gap:14px;font-size:25px;letter-spacing:1px;color:var(--blue-mid)}

/* problem band */
.band{left:0;top:985px;width:1200px;height:598px;background:linear-gradient(180deg,#2f5c78 0%,#4c7b8e 55%,#6a97a2 100%)}
.band-strip{left:0;top:1393px;width:1200px;height:155px;background:linear-gradient(90deg,rgba(0,187,165,.55),rgba(0,171,142,.85) 50%,rgba(103,215,201,.55))}
.band-title{left:0;top:1408px;width:1200px;text-align:center;font-size:50px;line-height:58px;letter-spacing:4px;color:var(--white);font-weight:500}

/* benefits */
.rule{left:57px;top:1953px;width:1003px;height:2px;background:var(--blue-mid)}
.rule-mark{left:1052px;top:1907px;width:86px;height:86px;border-radius:50%;background:var(--green-deep)}
.section-title{left:0;top:2000px;width:1200px;text-align:center;font-size:50px;letter-spacing:5px;font-weight:500}
.benefit{left:52px;width:440px;height:75px}
.benefit-bar{position:absolute;left:0;top:0;width:11px;height:75px}
.benefit-label{position:absolute;left:47px;top:16px;font-size:31px;letter-spacing:2px;color:var(--green-deep)}
.benefit-line{position:absolute;left:50px;top:74px;width:390px;height:2px;background:var(--blue)}
.benefit-photo{left:557px;top:2121px;width:614px;height:486px;border-radius:22px;background:linear-gradient(135deg,#7b4a34 0%,#3a3f47 45%,#5f6b76 100%)}

/* join */
.join-photo{left:0;top:2665px;width:1200px;height:600px;background:linear-gradient(90deg,#4d6f96 0%,#c9a896 30%,#dfe7ef 62%,#ffffff 80%)}
.join-text{right:54px;top:2712px;text-align:right;font-size:33px;line-height:36px;letter-spacing:2px;color:var(--blue-mid)}

/* footer */
.foot-mark{left:82px;top:3355px;width:86px;height:86px;border-radius:50%;background:var(--green-deep)}
.foot-divider{left:250px;top:3297px;width:3px;height:210px;background:var(--blue-soft)}
.foot-item{display:flex;align-items:center;font-size:19px;letter-spacing:.5px;color:var(--blue)}
.foot-icon{width:26px;height:26px;margin-right:24px}
.foot-flag{width:26px;height:18px;margin-right:16px}
.copyright{left:0;top:3530px;width:1200px;height:70px;background:var(--blue);color:var(--white);font-size:19px;letter-spacing:.5px;display:flex;align-items:center;justify-content:center}
</style>
</head>
<body>

<header>
  <div class="abs hero" role="img" aria-label="Photo of two hands gently holding each other"></div>
  <div class="abs brand">
    <span class="brand-mark"></span>
    <span class="brand-name">FERNBRIGHT HEALTH</span>
  </div>
  <nav class="abs nav">
    <a href="#">SOLUTION</a>
    <a href="#">ABOUT US</a>
    <a href="#">CONTACT</a>
  </nav>
  <div class="abs hero-accent"></div>
  <h1 class="abs hero-title">Guide You to<br>True Future<br>Healtcare</h1>
</header>

<section>
  <p class="abs lead" style="top:670px">We are healthcare technology<br>services company that’s guide you<br>to get new True Future Healthcare</p>
  <svg class="abs tri" style="left:1059px;top:659px" viewBox="0 0 112 161"><path d="M112 0 V161 H70 L0 80 L70 0 Z" fill="var(--blue-pale)"/></svg>
  <a class="abs btn" style="left:141px;top:848px;width:243px">ABOUT US</a>
  <a class="abs more" style="left:433px;top:862px">
    <svg width="24" height="24" viewBox="0 0 24 24" fill="none" stroke="var(--blue-mid)" stroke-width="2.5"><path d="M4 4 L12 12 L4 20 M12 4 L20 12 L12 20"/></svg>
    visit our profile
  </a>
</section>

<section>
  <div class="abs band" role="img" aria-label="Photo of hands typing on a laptop beside a stethoscope"></div>
  <div class="abs band-strip"></div>
  <h2 class="abs band-title">THE BIGGEST PUBLIC<br>HEALTCARE PROBLEM?</h2>
</section>

<section>
  <p class="abs lead" style="top:1655px">We are identifying lowest cost healthcare<br>coverage methods, including insurance,<br>discount cards, and cash options</p>
  <svg class="abs tri" style="left:1059px;top:1644px" viewBox="0 0 112 161"><path d="M112 0 V161 H70 L0 80 L70 0 Z" fill="var(--blue-pale)"/></svg>
  <a class="abs btn" style="left:141px;top:1833px;width:319px">OUR FEATURE</a>
  <a class="abs more" style="left:506px;top:1847px">
    <svg width="24" height="24" viewBox="0 0 24 24" fill="none" stroke="var(--blue-mid)" stroke-width="2.5"><path d="M4 4 L12 12 L4 20 M12 4 L20 12 L12 20"/></svg>
    learn more
  </a>
</section>

<section>
  <div class="abs rule"></div>
  <div class="abs rule-mark"></div>
  <h2 class="abs section-title">BENEFITS</h2>

  <div class="abs benefit" style="top:2121px"><span class="benefit-bar" style="background:var(--blue-deep)"></span><span class="benefit-label">Feature Benefit 1</span><span class="benefit-line"></span></div>
  <div class="abs benefit" style="top:2217px"><span class="benefit-bar" style="background:var(--blue)"></span><span class="benefit-label">Feature Benefit 2</span><span class="benefit-line"></span></div>
  <div class="abs benefit" style="top:2313px"><span class="benefit-bar" style="background:var(--blue-mid)"></span><span class="benefit-label">Feature Benefit 3</span><span class="benefit-line"></span></div>
  <div class="abs benefit" style="top:2409px"><span class="benefit-bar" style="background:var(--blue-soft)"></span><span class="benefit-label">Feature Benefit 4</span><span class="benefit-line"></span></div>
  <div class="abs benefit" style="top:2505px"><span class="benefit-bar" style="background:var(--blue-pale)"></span><span class="benefit-label">Feature Benefit 5</span><span class="benefit-line"></span></div>

  <div class="abs benefit-photo" role="img" aria-label="Photo of a laptop showing an analytics dashboard on a desk"></div>
</section>

<section>
  <div class="abs join-photo" role="img" aria-label="Photo of several hands clasped together in teamwork"></div>
  <p class="abs join-text">We are committed<br>to realizing the best<br>health technology<br>services for<br>your future</p>
  <a class="abs btn" style="left:947px;top:3059px;width:196px">JOIN</a>
  <a class="abs more" style="left:927px;top:3153px">
    <svg width="24" height="24" viewBox="0 0 24 24" fill="none" stroke="var(--blue-mid)" stroke-width="2.5"><path d="M4 4 L12 12 L4 20 M12 4 L20 12 L12 20"/></svg>
    start services
  </a>
</section>

<footer>
  <div class="abs foot-mark"></div>
  <div class="abs foot-divider"></div>

  <div class="abs foot-item" style="left:288px;top:3297px">
    <svg class="foot-icon" viewBox="0 0 24 24" fill="none" stroke="var(--blue-mid)" stroke-width="1.6"><path d="M5 3 L9 3 L10.5 8 L8 9.5 C9 12 12 15 14.5 16 L16 13.5 L21 15 L21 19 C21 20 20 21 19 21 C10 21 3 14 3 5 C3 4 4 3 5 3 Z"/></svg>
    Phone Number
  </div>
  <div class="abs foot-item" style="left:288px;top:3357px">
    <svg class="foot-icon" viewBox="0 0 24 24" fill="none" stroke="var(--blue-mid)" stroke-width="1.6"><rect x="3" y="6" width="18" height="13"/><path d="M3 6 L12 13 L21 6"/></svg>
    Email Address
  </div>
  <div class="abs foot-item" style="left:288px;top:3422px">
    <svg class="foot-icon" viewBox="0 0 24 24" fill="none" stroke="var(--blue-mid)" stroke-width="1.6"><rect x="7" y="3" width="10" height="6"/><rect x="3" y="9" width="18" height="8"/><rect x="7" y="14" width="10" height="7"/></svg>
    Fax
  </div>

  <div class="abs foot-item" style="left:665px;top:3297px"><svg class="foot-flag" viewBox="0 0 26 18"><path d="M0 9 L8 0 H26 V18 H8 Z" fill="var(--green-mid)"/></svg>Solutions</div>
  <div class="abs foot-item" style="left:665px;top:3357px"><svg class="foot-flag" viewBox="0 0 26 18"><path d="M0 9 L8 0 H26 V18 H8 Z" fill="var(--green-mid)"/></svg>About Us</div>
  <div class="abs foot-item" style="left:665px;top:3422px"><svg class="foot-flag" viewBox="0 0 26 18"><path d="M0 9 L8 0 H26 V18 H8 Z" fill="var(--green-mid)"/></svg>Contact</div>

  <div class="abs foot-item" style="left:922px;top:3297px"><svg class="foot-flag" viewBox="0 0 26 18"><path d="M0 9 L8 0 H26 V18 H8 Z" fill="var(--green-mid)"/></svg>Privacy Policy</div>
  <div class="abs foot-item" style="left:922px;top:3357px"><svg class="foot-flag" viewBox="0 0 26 18"><path d="M0 9 L8 0 H26 V18 H8 Z" fill="var(--green-mid)"/></svg>Terms and Use</div>

  <div class="abs copyright">2022 Fernbright Health. All rights reserved.</div>
</footer>

</body>
</html>
```